Cover for new song release

Song title: “Paper Lantern”. It’s a song about being in the moment. (Verse lyrics: “You can have your eyes wide open and still not even know...For every two steps forward take Paper Lantern and take in all the beauty all around.”

```html
<!DOCTYPE html>
<html lang="en">
<head>
<meta charset="utf-8">
<title>Paper Lantern — Single Cover</title>
<link rel="stylesheet" href="https://fonts.googleapis.com/css2?family=EB+Garamond:wght@400&display=swap">
<style>
  :root {
    --sleeve-white: #f1f1f2;
    --sky-teal-deep: #1f4d57;
    --sky-teal: #2e7680;
    --sky-haze: #7a9aa0;
    --sunset-pink: #e8a58f;
    --sunset-orange: #d9774f;
    --dusk-shadow: #4a3a3c;
    --ground-black: #0c0c0f;
    --title-white: #eef0f2;
  }
  * { margin: 0; padding: 0; box-sizing: border-box; }
  html, body {
    width: 1200px;
    height: 1200px;
    overflow: hidden;
    background: var(--sleeve-white);
  }
  .cover {
    position: relative;
    width: 1200px;
    height: 1200px;
    padding: 43px;
    background: var(--sleeve-white);
  }
  .cover-artwork {
    position: relative;
    width: 100%;
    height: 100%;
    overflow: hidden;
  }
  .sunset-photo {
    position: absolute;
    inset: 0;
    background:
      radial-gradient(ellipse 45% 30% at 80% 72%, rgba(240, 180, 160, 0.85), transparent 70%),
      radial-gradient(ellipse 60% 18% at 40% 66%, rgba(217, 119, 79, 0.45), transparent 75%),
      linear-gradient(180deg,
        var(--sky-teal-deep) 0%,
        var(--sky-teal) 22%,
        var(--sky-haze) 42%,
        var(--dusk-shadow) 58%,
        var(--sunset-pink) 72%,
        var(--sunset-orange) 88%,
        var(--ground-black) 92%,
        var(--ground-black) 100%);
  }
  .song-title {
    position: absolute;
    left: 0;
    right: 0;
    top: 35.3%;
    transform: translateY(-50%);
    text-align: center;
    font-family: "EB Garamond", Georgia, serif;
    font-weight: 400;
    font-size: 74px;
    letter-spacing: 0.5px;
    color: var(--title-white);
  }
</style>
</head>
<body>
  <main class="cover">
    <div class="cover-artwork">
      <div class="sunset-photo" role="img" aria-label="Painterly photo of a teal sky fading into a pink and orange sunset, with a lone silhouetted figure walking along a dark waterfront promenade"></div>
      <h1 class="song-title">Paper Lantern</h1>
    </div>
  </main>
</body>
</html>
```